Visitenkarten
Zielgruppe
Hallo!
Für mein Unternehmen habe ich bereits einmal ein Logo mit Feldmotte erstellen lassen (leider weiß ich den Designer nicht mehr).
Unter meinem Unternehmen Vollmerhaus Coaching laufen zwei Unternehmensbereiche, für die ich jetzt Visitenkarten benötige. Daher ist der Stil der beiden Teilbereiche ähnlich. Die Logos existieren schon. Nun benötige ich für beide Bereiche Visitenkarten. Für beide Bereiche benötige ich im Anschluss im 1:1 Auftrage noch Dateien, damit die ich Logos auch gut auf Webseiten und Social Medien nutzen kann.
Vollmerhaus HR Services <: bietet HR Dienstleistungen rund um das Personalwesen an: HR-Trainings, HR Outsourcing und Projekt- und Interimsmanagement
Sattelklar Balance | Vollmerhaus Coaching: bietet Mental- und Hypnosecoachings an, Trainings zur mentalen Fitness, Stress- und Blockadenlösung im Reitsport und optimale Turniervorbereitung
Aufgabenstellung
Bitte den bestehenden Brandguide und die Materialien nutzen. Eigene Ideen sind willkommen, sollen aber in der Logik bleiben.
Daten Visitenkarte Vollmerhaus HR Services:
Annelie Vollmerhaus
Dipl. Sozialwirt, Business Coach, Mentaltrainer
Telefon +49 (0)1593 26 48 357
Mobil +49 (0)171 58 93 704
Mail: annelie@vollmerhaus-beratung.example
Vollmerhaus HR Services | Vollmerhaus Coaching
Am Lindenhang 9b
31872 Hohenwald
Daten Visitenkarte Vollmerhaus Sattelklar Balance:
Dipl. Sozialwirt, Hypnosecoach, Mentaltrainer
Sattelklar Balance | Vollmerhaus Coaching

```html
<!DOCTYPE html>
<html lang="de">
<head>
<meta charset="utf-8">
<title>Visitenkarten Vollmerhaus</title>
<link rel="stylesheet" href="https://fonts.googleapis.com/css2?family=Montserrat:wght@400;500;700&display=swap">
<style>
  :root {
    --backdrop: #e9e9ed;
    --paper: #f3f2f6;
    --lavender: #cbc8dc;
    --purple: #6453a8;
    --purple-dark: #3f3666;
    --ink: #3a3360;
    --ink-soft: #5e5a78;
  }
  * { box-sizing: border-box; margin: 0; padding: 0; }
  html, body { width: 1000px; height: 1200px; overflow: hidden; }
  body {
    background: var(--backdrop);
    font-family: "Montserrat", sans-serif;
    color: var(--ink);
  }
  .sheet {
    width: 1000px; height: 1200px;
    display: grid;
    grid-template-columns: 440px 440px;
    grid-template-rows: 260px 260px;
    column-gap: 40px;
    row-gap: 180px;
    align-content: center;
    justify-content: center;
  }
  .card {
    position: relative;
    width: 440px; height: 260px;
    background: var(--paper);
    overflow: hidden;
    box-shadow: 0 6px 18px rgba(40, 36, 70, 0.12);
  }
  .card-art { position: absolute; inset: 0; width: 440px; height: 260px; }
  .contact { position: absolute; left: 28px; top: 26px; }
  .contact-name { font-size: 15px; font-weight: 700; letter-spacing: 0.3px; text-transform: uppercase; }
  .contact-title { font-size: 10px; color: var(--ink-soft); margin-top: 3px; }
  .contact-lines { margin-top: 18px; font-size: 10px; line-height: 17px; }
  .contact-lines dt { float: left; width: 52px; font-weight: 700; text-align: right; }
  .contact-lines dd { margin-left: 58px; }
  .contact-lines dd::before { content: ": "; }
  .contact-address { margin-top: 16px; font-size: 10px; line-height: 14px; color: var(--ink-soft); font-style: normal; }
  .brand-name {
    position: absolute;
    font-weight: 700;
    color: var(--ink);
    text-transform: uppercase;
    letter-spacing: 1px;
  }
  .brand-main { left: 28px; bottom: 34px; font-size: 20px; line-height: 24px; }
  .brand-riding { left: 170px; top: 92px; font-size: 15px; line-height: 20px; }
  .horse-illustration {
    position: absolute; left: 40px; top: 150px;
    width: 100px; height: 100px;
    background: radial-gradient(circle at 50% 50%, #b7b1d6 0%, #dcd9ea 60%, var(--paper) 100%);
    border-radius: 6px;
  }
</style>
</head>
<body>
<main class="sheet">

  <section class="card card-contact" aria-label="Rückseite Vollmerhaus HR Services">
    <svg class="card-art" viewBox="0 0 440 260" aria-hidden="true">
      <polygon points="170,0 440,0 440,180 380,30 200,30" fill="var(--lavender)"/>
      <polygon points="392,30 412,30 440,96 440,146" fill="var(--purple-dark)"/>
      <polygon points="0,246 440,196 440,260 0,260" fill="var(--purple)"/>
    </svg>
    <div class="contact">
      <h1 class="contact-name">Annelie Vollmerhaus</h1>
      <p class="contact-title">Dipl. Sozialwirt, Business Coach, Mentaltrainer</p>
      <dl class="contact-lines">
        <dt>Telefon</dt><dd>+49 (0)1593 26 48 357</dd>
        <dt>Mobil</dt><dd>+49 (0)171 58 93 704</dd>
        <dt>Mail</dt><dd>annelie@vollmerhaus-beratung.example</dd>
      </dl>
      <address class="contact-address">
        Vollmerhaus HR Services | Vollmerhaus Coaching<br>
        Am Lindenhang 9b<br>
        31872 Hohenwald
      </address>
    </div>
  </section>

  <section class="card card-front" aria-label="Vorderseite Vollmerhaus Coaching">
    <svg class="card-art" viewBox="0 0 440 260" aria-hidden="true">
      <polygon points="170,0 260,0 360,130 260,260 170,260 270,130" fill="var(--lavender)"/>
      <polygon points="262,0 306,0 406,130 306,260 262,260 362,130" fill="var(--purple-dark)"/>
      <polygon points="330,0 390,0 440,66 440,194 390,260 330,260 430,130" fill="var(--purple)"/>
    </svg>
    <p class="brand-name brand-main">Vollmerhaus<br>Coaching</p>
  </section>

  <section class="card card-contact" aria-label="Rückseite Sattelklar Balance">
    <svg class="card-art" viewBox="0 0 440 260" aria-hidden="true">
      <polygon points="170,0 440,0 440,180 380,30 200,30" fill="var(--lavender)"/>
      <polygon points="392,30 412,30 440,96 440,146" fill="var(--purple-dark)"/>
      <polygon points="0,246 440,196 440,260 0,260" fill="var(--purple)"/>
    </svg>
    <div class="contact">
      <h1 class="contact-name">Annelie Vollmerhaus</h1>
      <p class="contact-title">Dipl. Sozialwirt, Business Coach, Mentaltrainer</p>
      <dl class="contact-lines">
        <dt>Telefon</dt><dd>+49 (0)1593 26 48 357</dd>
        <dt>Mobil</dt><dd>+49 (0)171 58 93 704</dd>
        <dt>Mail</dt><dd>annelie@vollmerhaus-beratung.example</dd>
      </dl>
      <address class="contact-address">
        Vollmerhaus HR Services | Vollmerhaus Coaching<br>
        Am Lindenhang 9b<br>
        31872 Hohenwald
      </address>
    </div>
  </section>

  <section class="card card-front" aria-label="Vorderseite Vollmerhaus Sattelklar Balance">
    <svg class="card-art" viewBox="0 0 440 260" aria-hidden="true">
      <polygon points="170,0 260,0 360,130 260,260 170,260 270,130" fill="var(--lavender)"/>
      <polygon points="262,0 306,0 406,130 306,260 262,260 362,130" fill="var(--purple-dark)"/>
      <polygon points="330,0 390,0 440,66 440,194 390,260 330,260 430,130" fill="var(--purple)"/>
    </svg>
    <div class="horse-illustration" role="img" aria-label="Linienzeichnung eines galoppierenden Pferdes in Violett"></div>
    <p class="brand-name brand-riding">Vollmerhaus<br>Sattelklar<br>Balance</p>
  </section>

</main>
</body>
</html>
```